Security Company Needs a Website *

We need a website that gives our clients information about the services we provide, methods of contacting us and landing page to advertise on social media sites.

We need five landing pages titled Home, About Us, Services, Contact Us and a Landing Page that can be linked to Chatterlane advertising.

About Us - Should have a section for Core Values & Ethics, Our Vision, Our Mission and Partners.

Services - This page should show the different categories which include CCTV, Security Alarms, Access Control and Fire Protection.

CCTV Service Description:
Closed circuit television (CCTV) has long been implemented by businesses as a surveillance tool in areas that need monitoring. With digital CCTV cameras, multiple video cameras transmit signals through a set of monitors. The cameras provide thorough surveillance of the area.

With vast technological improvements over the last ten years, businesses with CCTV systems can use unique IP cameras and video analytics to monitor traffic flows, people-count, implement facial and number plate recognition. Useful information about customer behaviour and demographics can be discovered too. CCTV helps prevent crime in many industries and can assist with the improvement of industrial processes, safety on transport systems and traffic monitoring.

Security Alarms Service Description:
Alarms systems are electronic devices programmed to alert people to specific dangers and detect intrusions, fire or theft. Security alarms, systems and access control monitoring combine to create an integrated surveillance solution, tailored to your business’ unique requirements. Our surveillance and alarm monitoring services are ideal for perimeter protection from unwanted intruders or potential dangers.

Access Control Services:
An access control system allows for the free flow of authorised personnel while denying entry to unwanted visitors. With walk-in thieves and trespassers shut out, you dramatically reduce your exposure to crime while increasing the security of your employees, visitors, information and assets.

* Control when and who is entering your premises
* Protect employees, assets and information
* Secure an area or sector
* Observe movement
* Integrate with other security systems

Our range of access control systems can be seamlessly linked to other systems in our portfolio. These include Fire Detection Systems, Intruder Alarms, CCTV, and Building Management. A common request involves the need for a CCTV camera to pan around and focus on a door that has been highlighted as a security risk by the access control system.

Fire Protection Service:
To Be Advised

The above copy-writing will also have to be changed.

Contact Us - This form needs to be simple and straightforward to gather the prospects information and we would like to have a call to action on this page. The Contact Us page should also have a wayfindr plot location of our office address.

We would also like to have a link to our chatterlane page on the website.

Target Market(s)

Commercial businesses, building construction developers and property managers.

Industry/Entity Type

Security

Number of Pages Required

5+ page

Font styles to use
Sans Serif

Colors

Designer to choose colors to be used in the design.

Requirements
Must have
• We need to have the same look and feel as well as website features as the following website:
• https://www.kovrangard.com.au/business-security/
• The website must be easy to use and easy to edit as well.

```html
<!DOCTYPE html>
<html lang="en">
<head>
<meta charset="utf-8">
<title>Lumora Security Solutions</title>
<link href="https://fonts.googleapis.com/css2?family=Montserrat:wght@400;500;600;700&family=Open+Sans:wght@400;600&display=swap" rel="stylesheet">
<style>
:root{
  --navy:#1b3a8f;
  --blue:#1f4fb8;
  --blue-deep:#16389a;
  --ink:#333;
  --muted:#666;
  --paper:#fff;
  --soft:#f6f7fa;
  --black:#050505;
}
*{margin:0;padding:0;box-sizing:border-box}
html,body{width:1200px;height:3455px;overflow:hidden}
body{font-family:"Open Sans",Arial,sans-serif;color:var(--ink);background:var(--paper);position:relative}
.abs{position:absolute}
h1,h2,h3,.nav a,.btn{font-family:"Montserrat",Arial,sans-serif}

/* header */
.site-header{position:absolute;top:0;left:0;width:1200px;height:88px;background:var(--paper);border-top:5px solid var(--blue);z-index:3}
.brand{position:absolute;left:86px;top:-10px;width:176px;height:176px;border-radius:50%;background:var(--paper);box-shadow:0 3px 10px rgba(0,0,0,.15);display:flex;flex-direction:column;align-items:center;justify-content:center;text-align:center}
.brand-name{font-family:"Montserrat",Arial,sans-serif;font-weight:600;color:var(--navy);font-size:17px;line-height:1.25;letter-spacing:.5px}
.nav{position:absolute;top:34px;left:654px;width:400px;height:20px}
.nav a{font-size:12px;font-weight:500;color:#222;text-decoration:none;position:absolute;top:0;white-space:nowrap}
.nav a.active{color:var(--blue)}
.search{position:absolute;left:1063px;top:18px;width:50px;height:50px;border:2px solid var(--navy);border-radius:50%;display:flex;align-items:center;justify-content:center}

/* hero */
.hero{position:absolute;top:88px;left:0;width:1200px;height:527px;background:linear-gradient(120deg,#5c6570 0%,#8b949c 35%,#3d5a52 55%,#7d8a8c 75%,#4f5a60 100%)}
.hero-title{position:absolute;left:670px;top:179px;width:339px;height:55px;background:rgba(40,80,175,.85);color:#fff;font-size:27px;font-weight:600;padding:11px 22px;letter-spacing:.5px}
.hero-text{position:absolute;left:670px;top:241px;width:442px;height:125px;background:rgba(20,20,20,.7);color:#f1f1f1;font-size:12px;line-height:27px;padding:14px 22px}
.dots{position:absolute;left:575px;top:500px;display:flex;gap:4px}
.dots span{width:13px;height:13px;border:2px solid #fff;border-radius:50%}
.dots span.on{background:var(--navy)}

/* service rows */
.service{position:absolute;left:0;width:1200px;height:435px;background:linear-gradient(90deg,#fff,#f4f6fa)}
.service .photo{position:absolute;top:0;height:100%}
.service h2{position:absolute;font-size:23px;font-weight:600;color:var(--navy);letter-spacing:.5px}
.service p{position:absolute;width:437px;font-size:11.5px;line-height:27.5px;color:#555}
.btn{position:absolute;display:inline-flex;align-items:center;justify-content:center;height:42px;padding:0 26px;border:2px solid var(--navy);border-radius:21px;color:var(--navy);font-size:12px;font-weight:600;text-decoration:none;letter-spacing:.5px;background:#fff}
.ticks{position:absolute;list-style:none;font-size:11.5px;color:#555}
.ticks li{height:31px;display:flex;align-items:center;gap:17px}

/* about */
.about{position:absolute;top:2354px;left:0;width:1200px;height:366px;background:linear-gradient(90deg,rgba(30,78,185,.94),rgba(33,82,190,.9)),linear-gradient(90deg,#243d7a,#5a6f9e);text-align:center;color:#fff}
.about h2{position:absolute;top:50px;width:100%;font-size:50px;font-weight:500;letter-spacing:1px}
.about p{position:absolute;top:141px;left:237px;width:726px;font-size:12px;line-height:29px;color:#eef}
.btn-light{border-color:#fff;color:#fff;background:transparent;left:484px;top:250px;height:47px;padding:0 22px}

/* vision */
.vision h2{position:absolute;left:594px;top:2776px;font-size:22px;font-weight:600;color:var(--navy)}
.vision p{position:absolute;left:594px;top:2822px;width:460px;font-size:11.5px;line-height:27px;color:#555}
.btn-solid{background:var(--blue-deep);color:#fff;border-color:var(--blue-deep);left:596px;top:3005px;height:46px;width:148px}

/* footer */
.site-footer{position:absolute;top:3107px;left:0;width:1200px;height:348px;background:var(--black);color:#fff}
.foot-brand{position:absolute;left:0;top:46px;width:100%;text-align:center;font-family:"Montserrat",Arial,sans-serif;font-weight:600;font-size:20px;letter-spacing:1px}
.foot-rule{position:absolute;left:87px;top:153px;width:1026px;border-top:1px solid #2a2a2a}
.contact{position:absolute;top:180px;display:flex;gap:18px;align-items:flex-start}
.contact .ic{width:52px;height:52px;border:2px solid #ddd;border-radius:50%;display:flex;align-items:center;justify-content:center;flex:none}
.contact h3{font-size:16px;font-weight:500;margin-top:2px}
.contact span{display:block;font-size:11px;line-height:20px;color:#ddd}
.copy{position:absolute;left:87px;top:308px;font-size:11px;color:#ddd}
.social{position:absolute;left:1074px;top:293px;display:flex;align-items:center;gap:8px;font-size:11px}
.social i{width:36px;height:36px;border:2px solid #ddd;border-radius:50%;display:block}
</style>
</head>
<body>

<header class="site-header">
  <div class="brand"><div class="brand-name">LUMORA<br>SECURITY<br>SOLUTIONS</div></div>
  <nav class="nav">
    <a class="active" style="left:0">HOME</a>
    <a style="left:124px">ABOUT US</a>
    <a style="left:210px">SERVICES</a>
    <a style="left:324px">CONTACT US</a>
  </nav>
  <div class="search"><svg width="18" height="18" viewBox="0 0 18 18"><circle cx="7.5" cy="7.5" r="5" fill="none" stroke="#1b3a8f" stroke-width="2.2"/><line x1="11" y1="11" x2="16" y2="16" stroke="#1b3a8f" stroke-width="2.4" stroke-linecap="round"/></svg></div>
</header>

<section class="hero" role="img" aria-label="Dome security camera mounted in a bright glass office building">
  <h1 class="hero-title">LUMORA SECURITY</h1>
  <p class="hero-text">Sed ut perspiciatis unde omnis iste natus error sit voluptatem accusanti doloremque laudantium, totam rem aperiam, eaque ipsa quae ab illo et quasi architecto beatae vitae dicta sunt explicabo.</p>
  <div class="dots"><span></span><span class="on"></span><span></span></div>
</section>

<section class="service" style="top:615px">
  <div class="photo" role="img" aria-label="Technician installing a ceiling CCTV camera" style="left:0;width:565px;background:linear-gradient(135deg,#e9ecef,#d6d9dc 40%,#e07a3a 60%,#3b4f9a 85%)"></div>
  <h2 style="left:606px;top:84px">CCTV SERVICE</h2>
  <p style="left:606px;top:130px">Closed circuit television (CCTV) has long been implemented by businesses as a surveillance tool in areas that need monitoring. With digital CCTV cameras, multiple video cameras transmit signals through a set of monitors. The cameras provide thorough surveillance of the area With vast technological improvements over the last ten years, businesses with CCTV systems can use unique With vast technological improvements over the last ten years</p>
  <a class="btn" style="left:608px;top:329px">READ MORE</a>
</section>

<section class="service" style="top:1050px;background:linear-gradient(90deg,#fdfbfa,#f5f1ee)">
  <div class="photo" role="img" aria-label="Finger pressing a wall-mounted alarm keypad" style="left:633px;width:567px;background:linear-gradient(120deg,#f2efec,#e5dfda 45%,#c99a7c 70%,#ece8e4)"></div>
  <h2 style="left:157px;top:74px">SECURITY ALARMS SERVICE</h2>
  <p style="left:157px;top:128px">Alarms systems are electronic devices programmed to alert people to specific dangers and detect intrusions, fire or theft. Security alarms, systems and access control monitoring combine to create an integrated surveillance solution, tailored to your business' unique requirements. Our surveillance and alarm monitoring services are ideal for perimeter protection from unwanted intruders or potential fire or theft. Security alarms,dangers</p>
  <a class="btn" style="left:161px;top:318px">READ MORE</a>
</section>

<section class="service" style="top:1485px">
  <div class="photo" role="img" aria-label="Hand holding an access card to a wall reader" style="left:0;width:565px;background:linear-gradient(110deg,#f3f3f3,#e6e6e6 40%,#d9b49a 55%,#eaeaea)"></div>
  <h2 style="left:606px;top:58px">ACCESS CONTROL SERVICES</h2>
  <p style="left:606px;top:110px">Closed circuit television (CCTV) has long been implemented by businesses as a surveillance tool in areas that need monitoring. With digital CCTV cameras, multiple video cameras transmit signals through a set of monitors.</p>
  <ul class="ticks" style="left:606px;top:203px">
    <li><svg width="12" height="10" viewBox="0 0 12 10"><path d="M1 5l3.5 3.5L11 1" fill="none" stroke="#1b3a8f" stroke-width="2.2"/></svg>Control when and who is entering your premises</li>
    <li><svg width="12" height="10" viewBox="0 0 12 10"><path d="M1 5l3.5 3.5L11 1" fill="none" stroke="#1b3a8f" stroke-width="2.2"/></svg>Protect employees, assets and information</li>
    <li><svg width="12" height="10" viewBox="0 0 12 10"><path d="M1 5l3.5 3.5L11 1" fill="none" stroke="#1b3a8f" stroke-width="2.2"/></svg>Secure an area or sector</li>
    <li><svg width="12" height="10" viewBox="0 0 12 10"><path d="M1 5l3.5 3.5L11 1" fill="none" stroke="#1b3a8f" stroke-width="2.2"/></svg>Observe movement</li>
    <li><svg width="12" height="10" viewBox="0 0 12 10"><path d="M1 5l3.5 3.5L11 1" fill="none" stroke="#1b3a8f" stroke-width="2.2"/></svg>Integrate with other security systems</li>
  </ul>
</section>

<section class="service" style="top:1921px;height:433px;background:linear-gradient(90deg,#fdfbfa,#f5f2ef)">
  <div class="photo" role="img" aria-label="Technician inspecting a red fire extinguisher with a clipboard" style="left:576px;width:624px;background:linear-gradient(120deg,#eeeae6,#d8d3cf 40%,#2f3c6e 60%,#c8282a 80%,#ece8e4)"></div>
  <h2 style="left:157px;top:88px">FIRE PROTECTION SERVICE</h2>
  <p style="left:157px;top:142px">Alarms systems are electronic devices programmed to alert people to specific dangers and detect intrusions, fire or theft. Security alarms, systems and access control monitoring combine to create an integrated surveillance solution, tailored to your business' unique requirements. Our surveillance and alarm monitoring services are ideal for perimeter protection from unwanted intruders or potential fire or theft. Security alarms,dangers</p>
  <a class="btn" style="left:161px;top:332px">READ MORE</a>
</section>

<section class="about">
  <h2>ABOUT US</h2>
  <p>Sed ut perspiciatis unde omnis iste natus error sit voluptatem accusantium doloremque laudantium, totam rem aperiam, eaque ipsa quae ab illo inventore veritatis et quasi architecto beatae vitae dicta sunt explicabo. Nemo enim ipsam voluptatem quia voluptas sit aut fugit, sed quia consequuntur magni dolores eos qui ratione voluptatem sequi nesciunt.</p>
  <a class="btn btn-light">CLICK HERE FOR MORE INFO</a>
</section>

<section class="vision">
  <div class="abs" role="img" aria-label="Technician in a blue shirt setting up a wall alarm panel" style="left:124px;top:2766px;width:424px;height:286px;background:linear-gradient(120deg,#b88f78,#d9c2b3 40%,#5f86c4 65%,#e3d6cc)"></div>
  <h2>OUR VISION &amp; MISSION</h2>
  <p>Sed ut perspiciatis unde omnis iste natus error sit voluptatem accusantium dol orem que laudantium, totam rem aperiam, eaque ipsa quae ab illo inventore veritatis et qu asi architecto beatae vitae dicta sunt explicabo. Nemo enim ipsam voluptatem qui a voluptas sit aspernatur aut odit aut fugit, sed quia consequuntur magni dolores eos qui ratione voluptatem sequi nesciunt.Neque porro quisquam est, qui dolorem ipsum quia dolor sit amet,consectetur, adipisci velit, sed quia non</p>
  <a class="btn btn-solid">READ MORE</a>
</section>

<footer class="site-footer">
  <div class="foot-brand">LUMORA<br>SECURITY SOLUTIONS</div>
  <div class="foot-rule"></div>
  <div class="contact" style="left:128px">
    <div class="ic"><svg width="16" height="20" viewBox="0 0 16 20"><path d="M8 1a6 6 0 0 0-6 6c0 4.5 6 12 6 12s6-7.5 6-12a6 6 0 0 0-6-6z" fill="#fff"/><circle cx="8" cy="7" r="2.2" fill="#050505"/></svg></div>
    <div><h3>Address :</h3><span># 48 Harrow Lane, Suite 12<br>Brookvale Park</span></div>
  </div>
  <div class="contact" style="left:522px">
    <div class="ic"><svg width="20" height="14" viewBox="0 0 20 14"><rect x="1" y="1" width="18" height="12" rx="1.5" fill="none" stroke="#fff" stroke-width="1.8"/><path d="M1.5 1.5L10 8l8.5-6.5" fill="none" stroke="#fff" stroke-width="1.8"/></svg></div>
    <div><h3>Email</h3><span>info@lumorasecurity.com</span></div>
  </div>
  <div class="contact" style="left:872px">
    <div class="ic"><svg width="18" height="18" viewBox="0 0 24 24"><path d="M6.6 10.8a15 15 0 0 0 6.6 6.6l2.2-2.2a1 1 0 0 1 1-.25 11.4 11.4 0 0 0 3.6.57 1 1 0 0 1 1 1V20a1 1 0 0 1-1 1A17 17 0 0 1 3 4a1 1 0 0 1 1-1h3.5a1 1 0 0 1 1 1c0 1.25.2 2.45.57 3.57a1 1 0 0 1-.25 1z" fill="#fff"/></svg></div>
    <div><h3>Phone</h3><span>Mobile : (000)-555-0148</span></div>
  </div>
  <p class="copy">© Copyrights 2018 Lumora Security All Rights Reserved.</p>
  <div class="social"><i></i>Chatterlane</div>
</footer>

</body>
</html>
```